Business card design needed

Chasing a very simplistic modern design with a logo incorporating "TRV".
I'm starting a plumbing business.
I do water, sanitary and drainage plumbing that will cover residential, commercial, rental, rural, excavation, new housing and all maintanence requirements.

Industry/Entity Type

Business

Contact Information for Business Card

TRV PLUMBING SERVICES
DEAN HOLLOWBY - LICENSED PLUMBER
PHONE: 0481926574
E-MAIL: hollodt7@wirelane.com
NORTHERN SUBURBS

Requirements
Must have
• lower case email address

```html
<!DOCTYPE html>
<html lang="en">
<head>
<meta charset="utf-8">
<title>TRV Plumbing Services – Business Card</title>
<link rel="stylesheet" href="https://fonts.googleapis.com/css2?family=Arimo:wght@400;700&display=swap">
<style>
  :root {
    --backdrop: #2b2b2d;
    --card: #1f1e1f;
    --blue: #1a8fd6;
    --blue-bright: #29a3ea;
    --grey: #b9babc;
    --ink: #1a1a1c;
  }
  * { box-sizing: border-box; margin: 0; padding: 0; }
  html, body {
    width: 1200px;
    height: 900px;
    overflow: hidden;
    background: var(--backdrop);
    font-family: "Arimo", Arial, sans-serif;
  }
  .sheet {
    width: 1200px;
    height: 900px;
    display: flex;
    flex-direction: column;
    align-items: center;
    justify-content: center;
    gap: 56px;
  }
  .card {
    position: relative;
    width: 630px;
    height: 360px;
    background: var(--card);
    box-shadow: 0 14px 34px rgba(0,0,0,0.45);
    overflow: hidden;
  }

  /* Back side – centred wordmark */
  .card--back {
    display: flex;
    align-items: center;
    justify-content: center;
  }
  .wordmark {
    display: flex;
    align-items: flex-end;
    gap: 14px;
    color: var(--blue);
    font-weight: 700;
    text-transform: uppercase;
    line-height: 0.9;
  }
  .wordmark__initials { font-size: 108px; letter-spacing: 2px; }
  .wordmark__trade { font-size: 26px; letter-spacing: 1px; padding-bottom: 10px; }

  /* Front side – contact details */
  .card--front .wordmark {
    position: absolute;
    left: 44px;
    top: 84px;
  }
  .card--front .wordmark__initials { font-size: 72px; }
  .card--front .wordmark__trade { font-size: 18px; padding-bottom: 6px; }

  .name-bar {
    position: absolute;
    left: 0;
    top: 168px;
    width: 330px;
    height: 34px;
    background: var(--blue-bright);
    padding-left: 44px;
    display: flex;
    align-items: center;
  }
  .name {
    color: var(--ink);
    font-size: 24px;
    font-weight: 700;
    letter-spacing: 0.5px;
  }
  .role {
    position: absolute;
    left: 44px;
    top: 212px;
    color: var(--grey);
    font-size: 15px;
    font-weight: 700;
  }
  .contact {
    position: absolute;
    left: 44px;
    top: 256px;
    font-size: 15px;
    font-weight: 700;
    line-height: 1.35;
    color: var(--grey);
  }
  .contact__label { color: var(--blue-bright); }
  .contact__area { color: var(--blue-bright); display: block; }
</style>
</head>
<body>
  <main class="sheet">
    <section class="card card--back" aria-label="Card back">
      <div class="wordmark">
        <span class="wordmark__initials">TRV</span>
        <span class="wordmark__trade">Plumbing<br>Services</span>
      </div>
    </section>

    <section class="card card--front" aria-label="Card front">
      <div class="wordmark">
        <span class="wordmark__initials">TRV</span>
        <span class="wordmark__trade">Plumbing<br>Services</span>
      </div>
      <div class="name-bar"><span class="name">DEAN HOLLOWBY</span></div>
      <p class="role">LICENSED PLUMBER</p>
      <p class="contact">
        <span class="contact__label">P:</span> 0481926574
        <span class="contact__label">E:</span> hollodt7@wirelane.com
        <span class="contact__area">NORTHERN SUBURBS</span>
      </p>
    </section>
  </main>
</body>
</html>
```